New bussiness card, using company logo.
Lachlan Voss
Manager/Director
Birch Property Developments
Po Box 4657
Larkfield Central
Vic
0455 386 218
lachlan@birchpropertydevelopments
eye catching, vibrant colours, professional

```html
<!DOCTYPE html>
<html lang="en">
<head>
<meta charset="utf-8">
<title>Birch Property Developments – Business Card</title>
<link rel="stylesheet" href="https://fonts.googleapis.com/css2?family=Noto+Sans:wght@400;700&display=swap">
<style>
  :root {
    --page-bg: #ffffff;
    --card-bg: #ffffff;
    --card-edge: #c9c9c9;
    --ink: #434e55;
    --accent-red: #d9141b;
    --accent-green: #6fe01c;
  }
  html, body {
    margin: 0;
    padding: 0;
    width: 1200px;
    height: 1000px;
    overflow: hidden;
    background: var(--page-bg);
  }
  .card {
    position: absolute;
    left: 97px;
    top: 175px;
    width: 1011px;
    height: 655px;
    background: var(--card-bg);
    border: 1px solid var(--card-edge);
    box-sizing: border-box;
    font-family: "Noto Sans", Verdana, sans-serif;
    color: var(--ink);
  }
  .brand {
    position: absolute;
    left: 655px;
    top: 108px;
    display: flex;
    align-items: center;
    gap: 8px;
  }
  .brand-mark {
    width: 14px;
    height: 14px;
    background: var(--accent-green);
  }
  .brand-name {
    font-size: 14px;
    font-weight: 700;
    letter-spacing: 0.2px;
    color: var(--accent-red);
    text-transform: uppercase;
    white-space: nowrap;
  }
  .details {
    position: absolute;
    left: 151px;
    top: 138px;
    font-size: 28px;
    line-height: 35px;
    letter-spacing: 0.3px;
  }
  .details p { margin: 0; white-space: nowrap; }
  .person-name { font-weight: 700; }
  .surname { color: var(--accent-red); }
  .company-name { font-weight: 700; }
  .company { margin-top: 70px; }
  .contact { margin-top: 34px; }
</style>
</head>
<body>
  <div class="card">
    <div class="brand">
      <span class="brand-mark"></span>
      <span class="brand-name">Birch Property Developments</span>
    </div>
    <div class="details">
      <div class="person">
        <p class="person-name">Lachlan <span class="surname">Voss</span></p>
        <p class="person-role">Manager/Director</p>
      </div>
      <div class="company">
        <p class="company-name">Birch Property Developments</p>
        <p>Po Box 4657</p>
        <p>Larkfield Central</p>
        <p>Vic</p>
      </div>
      <div class="contact">
        <p class="phone">0455 386 218</p>
        <p class="email">lachlan@birchpropertydevelopments</p>
      </div>
    </div>
  </div>
</body>
</html>
```